Key Scientific Research Plastics Presentation - 5 Slides

We need the attached slides reworked with the following changes:

Information needs to be very visually stunning and easily understood
Text/font treatments should attract attention
All graphs and infographics can be recreated to match style
Attached color palette is not necessary, but can be used

Please reach out with any questions.

```html
<!DOCTYPE html>
<html lang="en">
<head>
<meta charset="utf-8">
<title>Plastics Research Presentation – Five Slides</title>
<link href="https://fonts.googleapis.com/css2?family=Poppins:wght@300;700&family=Roboto:ital,wght@0,400;0,500;0,700;1,400;1,700&display=swap" rel="stylesheet">
<style>
:root{
  --canvas:#bcbcbc;
  --paper:#ffffff;
  --ink:#222222;
  --body:#3c3c3c;
  --muted:#555555;
  --gold:#c4930f;
  --gold-deep:#b8860b;
  --olive:#9a9a12;
  --lime:#9cb325;
  --orange:#d08a1f;
  --brown:#7a4a1a;
  --cream:#fdf6e6;
  --rule:#e3e3e3;
  --red:#d62a2a;
  --green:#4fa12f;
  --amber:#f2b705;
}
*{margin:0;padding:0;box-sizing:border-box}
html,body{width:1200px;height:1085px;overflow:hidden;background:var(--canvas)}
body{position:relative;font-family:'Roboto',sans-serif;color:var(--body)}
.slide{position:absolute;width:545px;height:306px;background:var(--paper);border-bottom:3px solid var(--orange);overflow:hidden}
.slide *{position:absolute}
.slide--treaty{left:37px;top:45px}
.slide--cities{left:618px;top:45px}
.slide--ngo{left:37px;top:387px}
.slide--risk{left:618px;top:387px}
.slide--eps{left:328px;top:730px}

.title{left:30px;top:18px;font-family:'Poppins',sans-serif;font-weight:700;font-size:17px;line-height:20px;color:var(--ink);letter-spacing:.1px}
.title .light{font-weight:300;display:block;position:static}
.brand{left:424px;top:12px;width:120px;height:49px}
.brand-mark{left:0;top:0;width:49px;height:49px;border-radius:50%;background:var(--gold)}
.brand-name{left:53px;top:15px;font-family:'Roboto',sans-serif;font-size:9px;line-height:9px;color:var(--brown);white-space:nowrap}
.footer-copy{left:30px;bottom:12px;font-size:7px;color:var(--ink)}
.footer-page{right:34px;bottom:12px;font-size:7px;color:var(--ink)}
.footer-copy::before{content:"©";position:static;margin-right:4px}

/* slide: treaty */
.quote-panel{left:69px;top:70px;width:192px;height:164px;background:linear-gradient(135deg,#4b4b4b,#2e2e2e);border-left:5px solid var(--olive)}
.quote-text{left:19px;top:45px;width:155px;font-size:6.6px;line-height:11.4px;font-style:italic;color:#fff}
.checklist{left:287px;top:72px;width:210px;height:160px;list-style:none}
.check{left:0;width:210px;font-size:6.6px;line-height:11.4px;color:var(--ink);padding-left:21px}
.check svg{left:0;top:-2px;width:15px;height:15px}
.banner{left:0;top:253px;width:545px;height:18px}
.banner-bar{top:0;height:18px;width:164px}
.banner-bar--left{left:0;background:linear-gradient(90deg,rgba(196,147,15,0),var(--gold-deep))}
.banner-bar--right{right:0;background:linear-gradient(90deg,var(--gold-deep),rgba(196,147,15,0))}
.banner-text{left:164px;width:216px;top:1px;text-align:center;font-family:'Roboto',sans-serif;font-weight:500;font-size:11.4px;color:var(--ink)}

/* slide: cities */
.step-num{left:29px;font-family:'Roboto',sans-serif;font-weight:700;font-style:italic;font-size:22px;color:var(--olive)}
.step-head{left:67px;font-weight:700;font-style:italic;font-size:11px;color:var(--gold)}
.step-body{left:67px;width:190px;font-size:6.6px;line-height:8.5px;color:var(--muted)}
.lab-visual{left:278px;top:58px;width:226px;height:226px}
.lab-caption{left:275px;top:227px;width:176px;height:52px;background:#fff;padding:6px 6px 0 6px;font-size:5.1px;line-height:8.5px;font-style:italic;color:var(--muted)}
.lab-caption span{position:static}

/* slide: ngo */
.lead{left:32px;width:350px;font-size:6.6px;line-height:11.4px;color:var(--body)}
.card{top:84px;width:231px;height:126px;border:1px solid var(--rule)}
.card--claim{left:32px}
.card--study{left:280px}
.badge{left:12px;top:5px;width:49px;height:52px;background:var(--cream);border:2px solid var(--orange)}
.thumb{left:16px;top:5px;width:53px;height:52px;background:linear-gradient(#f4f4f4,#e2e2e2);border:1px solid #cfcfcf}
.card-text{top:6px;font-weight:700;font-size:7.4px;line-height:9.9px;color:var(--gold);text-align:justify}
.card--claim .card-text{left:75px;width:143px}
.card--study .card-text{left:81px;width:132px}
.card-ref{left:75px;top:72px;width:145px;font-weight:700;font-size:6px;line-height:10px;color:var(--ink)}

/* slide: risk */
.note{left:32px;width:490px;font-size:6.5px;line-height:11.3px;font-style:italic;color:var(--body)}
.ratings-label{left:32px;top:137px;font-weight:700;font-size:6.5px;color:var(--ink)}
.ratings{left:33px;top:150px;width:252px;height:94px;border:1px solid var(--rule)}
.ratings-col{top:0;height:92px;width:126px}
.ratings-col--a{left:0;border-right:1px solid var(--rule)}
.ratings-col--b{left:126px}
.ratings-head{left:0;top:0;width:100%;height:19px;background:var(--cream);font-weight:700;font-size:6.4px;line-height:19px;padding-left:7px;color:var(--gold)}
.ratings-body{left:7px;top:22px;width:113px;font-size:5.6px;line-height:11.3px;color:var(--ink);text-align:justify}
.exposure-map{left:250px;top:120px;width:200px;height:160px}
.risk-note{left:453px;top:160px;width:80px;font-style:italic;font-size:6.5px;line-height:11.4px;color:var(--gold)}

/* slide: eps */
.sub{left:32px;top:65px;font-weight:700;font-size:6.6px;color:var(--gold);letter-spacing:.1px}
.emissions{left:32px;top:92px;width:243px;height:118px;border:1px solid var(--rule)}
.emissions-head{top:0;height:21px;font-family:'Roboto',sans-serif;font-weight:700;font-size:6.6px;line-height:21px;color:#fff;text-align:center}
.emissions-head--scenario{left:0;width:122px;background:var(--gold-deep)}
.emissions-head--life{left:122px;width:121px;background:var(--olive)}
.emissions-split{left:121px;top:21px;width:1px;height:97px;background:var(--rule)}
.row-label,.row-value{font-size:7px;line-height:9px;color:var(--body)}
.row-label{left:22px}
.row-value{left:145px}
.row-rule{left:0;width:243px;height:1px;background:#efefef}
.chart{left:285px;top:80px;width:245px;height:184px}
</style>
</head>
<body>

<!-- Slide 01 -->
<section class="slide slide--treaty">
  <h1 class="title">GEA PLASTIC POLLUTION TREATY<span class="light">SCIENTIFIC CHECKS &amp; BALANCES</span></h1>
  <div class="brand"><span class="brand-mark"></span><span class="brand-name">Foam Science<br>Alliance</span></div>
  <div class="quote-panel" role="img" aria-label="Photograph of a worker sorting plastic waste, dimmed behind a quote">
    <p class="quote-text">Some think science can provide definitive, complete and foolproof answers. But given the world’s complexity, different research modalities and replication limits, critical thinking must be embraced to develop policies that work.</p>
  </div>
  <ul class="checklist">
    <li class="check" style="top:0">
      <svg viewBox="0 0 16 16"><circle cx="8" cy="8" r="7" fill="none" stroke="var(--green)" stroke-width="1.2"/><path d="M5 8.2l2 2 4-4.2" fill="none" stroke="var(--green)" stroke-width="1.6"/></svg>The Body of Research on Plastic Is Extensive.</li>
    <li class="check" style="top:22px">
      <svg viewBox="0 0 16 16"><circle cx="8" cy="8" r="7" fill="none" stroke="var(--amber)" stroke-width="1.2"/><text x="8" y="11" font-size="8" text-anchor="middle" fill="var(--amber)" font-family="Roboto">?</text></svg>Are All Plastics Toxic?</li>
    <li class="check" style="top:45px">
      <svg viewBox="0 0 16 16"><circle cx="8" cy="8" r="7" fill="none" stroke="var(--amber)" stroke-width="1.2"/><text x="8" y="11" font-size="8" text-anchor="middle" fill="var(--amber)" font-family="Roboto">?</text></svg>Are NGO, GEA or Industry Interpretations Accurate or Inaccurate?</li>
    <li class="check" style="top:79px">
      <svg viewBox="0 0 16 16"><circle cx="8" cy="8" r="7" fill="none" stroke="var(--red)" stroke-width="1.2"/><path d="M5.5 5.5l5 5M10.5 5.5l-5 5" stroke="var(--red)" stroke-width="1.6"/></svg>Is Data Transparency Evident For The Science Supporting Policy Considerations?</li>
    <li class="check" style="top:113px">
      <svg viewBox="0 0 16 16"><circle cx="8" cy="8" r="7" fill="none" stroke="var(--amber)" stroke-width="1.2"/><text x="8" y="11" font-size="8" text-anchor="middle" fill="var(--amber)" font-family="Roboto">?</text></svg>Problematic Plastics Are Classified Without Criteria</li>
    <li class="check" style="top:136px">
      <svg viewBox="0 0 16 16"><circle cx="8" cy="8" r="7" fill="none" stroke="var(--green)" stroke-width="1.2"/><path d="M5 8.2l2 2 4-4.2" fill="none" stroke="var(--green)" stroke-width="1.6"/></svg>Is Scientific Information On Plastic Pollution Being Used Out Of Context?</li>
  </ul>
  <div class="banner">
    <span class="banner-bar banner-bar--left"></span>
    <p class="banner-text">Know How To Ask The Right Questions</p>
    <span class="banner-bar banner-bar--right"></span>
  </div>
  <p class="footer-copy">Copyrights 2024 | All Rights Reserved</p>
  <p class="footer-page">Page No : 01</p>
</section>

<!-- Slide 03 -->
<section class="slide slide--cities">
  <h1 class="title">ATMOSPHERIC STUDIES IN 11 CITIES<br>HAVE VARYING RESULTS</h1>
  <div class="brand"><span class="brand-mark"></span><span class="brand-name">Foam Science<br>Alliance</span></div>

  <p class="step-num" style="top:66px">01</p>
  <h2 class="step-head" style="top:69px">Thematic Hypothesis</h2>
  <p class="step-body" style="top:87px">Atmospheric transport of microplastics is detrimental and is of great concern to the global community.</p>

  <p class="step-num" style="top:111px">02</p>
  <h2 class="step-head" style="top:114px">What’s Inside</h2>
  <p class="step-body" style="top:132px">There Are Three (3) Air Sampling Methodologies In This Developing Field of Study</p>
  <p class="step-body" style="top:157px">No Standard Method Exists To Prepare Airborne Microplastic Test Samples</p>
  <p class="step-body" style="top:183px">Visual Identification Methods Are Ineffective For Smaller Atmospheric Samples</p>
  <p class="step-body" style="top:208px">Studies Have Shown a Dominant Number of Airborne Microplastics are Fibers (≤95%).</p>

  <p class="step-num" style="top:233px">03</p>
  <h2 class="step-head" style="top:236px">Bottom Line</h2>
  <p class="step-body" style="top:254px">There is a need to conduct comprehensive research on sources of atmospheric microplastics to aid in the</p>

  <svg class="lab-visual" viewBox="0 0 226 226">
    <defs>
      <linearGradient id="labTone" x1="0" y1="0" x2="1" y2="1">
        <stop offset="0" stop-color="#cfe6f2"/><stop offset=".5" stop-color="#5fa3c4"/><stop offset="1" stop-color="#1f4f6e"/>
      </linearGradient>
    </defs>
    <circle cx="113" cy="110" r="106" fill="none" stroke="var(--gold)" stroke-width="2"/>
    <circle cx="113" cy="110" r="101" fill="url(#labTone)" role="img" aria-label="Photograph of a scientist examining plastic bottles in a laboratory"/>
  </svg>
  <p class="lab-caption"><span>In 11 studies in specific locations (Europe, Asia, North America) airborne polystyrene particles were found in only three cities. The results represent three different test sample types and all three used varying air concentration calculations. Therefore, the results are incompatible.</span></p>

  <p class="footer-copy">Copyrights 2024 | All Rights Reserved</p>
  <p class="footer-page">Page No : 03</p>
</section>

<!-- Slide 02 -->
<section class="slide slide--ngo">
  <h1 class="title">NGO MISUSE OF TECHNICAL DATA</h1>
  <p class="lead" style="top:44px">The definition of data misuse is using any information in a way it’s not supposed to be used. Terms of proper data use are usually specified in laws, industry standards, policies, and other agreements.</p>
  <div class="brand"><span class="brand-mark"></span><span class="brand-name">Foam Science<br>Alliance</span></div>

  <article class="card card--claim">
    <div class="badge" role="img" aria-label="Coastal Waste Coalition badge"></div>
    <p class="card-text">False Claim: “Polystyrene foam contains styrene, which has been linked to cancer, vision and hearing loss, impaired memory and concentration, and nervous system effects.”</p>
    <p class="card-ref">Reference: Potential Toxicity of Polystyrene Micropolastics</p>
  </article>

  <article class="card card--study">
    <div class="thumb" role="img" aria-label="Cover page of a research journal article on polystyrene microplastic toxicity"></div>
    <p class="card-text">Research Conclusions: “The study confirmed that PS particles were not toxic to human cells at a dosage of ~500µg/mL and PS particles with diameters of 10-11 µm were not significantly cytotoxic”. Further, “It could be concluded that PS particles are not cytotoxic to HDFs and PBMCs in usual conditions but might cause damage in extreme, high concentrations.”</p>
  </article>

  <p class="footer-copy">Copyrights 2024 | All Rights Reserved</p>
  <p class="footer-page">Page No : 02</p>
</section>

<!-- Slide 04 -->
<section class="slide slide--risk">
  <h1 class="title">UNDERSTANDING RISK VERSUS<br>EXPOSURE</h1>
  <div class="brand"><span class="brand-mark"></span><span class="brand-name">Foam Science<br>Alliance</span></div>
  <p class="lead" style="top:59px;width:290px">Any substance can be poisonous. Chemicals of concern must be evaluated within typical use parameters to evaluate its potential to present a hazard.</p>
  <p class="note" style="top:88px">U.S. National Risk Review System (NRRS) cautions that “NRRS values cannot be validly used to accurately predict the incidence of human disease or the type of effects that chemical exposures have on humans. This is due to the numerous uncertainties involved in risk assessment, including those associated with extrapolations from animal data to humans and from high experimental doses to lower environmental exposures.”</p>

  <p class="ratings-label">Is It Toxic? Scientific Ratings</p>
  <div class="ratings">
    <div class="ratings-col ratings-col--a">
      <p class="ratings-head">Carcinogens</p>
      <p class="ratings-body">“no significant risk level” (“NSRL”) means that exposure to the amount of chemical in a product would result in no more than one case of cancer out of every 100,000 individuals who were exposed to the chemical over a 70-year time period.</p>
    </div>
    <div class="ratings-col ratings-col--b">
      <p class="ratings-head">Reproductive Toxins</p>
      <p class="ratings-body" style="text-align:left">Maximum allowable dose level (“MADL”) is the level at which a chemical would have no observable effect, even if an individual were exposed to 1,000 times that level</p>
    </div>
  </div>

  <svg class="exposure-map" viewBox="250 120 200 160">
    <path d="M354 133 A80 80 0 0 1 354 266" fill="none" stroke="var(--gold)" stroke-width=".7"/>
    <line x1="351" y1="180" x2="374" y2="159" stroke="var(--gold)" stroke-width=".6"/>
    <line x1="371" y1="199" x2="391" y2="199" stroke="var(--gold)" stroke-width=".6"/>
    <line x1="351" y1="218" x2="374" y2="240" stroke="var(--gold)" stroke-width=".6"/>
    <circle cx="340" cy="199" r="31" fill="#fff" stroke="var(--gold)" stroke-width=".8"/>
    <circle cx="340" cy="199" r="24" fill="var(--gold-deep)"/>
    <text x="340" y="197" font-family="Roboto" font-weight="700" font-size="4.6" fill="#fff" text-anchor="middle">RISK OF</text>
    <text x="340" y="204" font-family="Roboto" font-weight="700" font-size="4.6" fill="#fff" text-anchor="middle">EXPOSURE</text>
    <g fill="var(--gold-deep)">
      <circle cx="354" cy="133" r="3.6"/><circle cx="374" cy="159" r="3.6"/><circle cx="391" cy="199" r="3.6"/><circle cx="374" cy="240" r="3.6"/><circle cx="354" cy="266" r="3.6"/>
    </g>
    <g font-family="Roboto" font-weight="500" font-size="8.4" fill="var(--ink)">
      <text x="363" y="136">Dose</text><text x="383" y="162">Toxicity</text><text x="400" y="202">Duration</text><text x="383" y="243">Frequency</text><text x="363" y="269">Route of Exposure</text>
    </g>
  </svg>
  <p class="risk-note">Risk Assessment Involves Reasonable Assumptions Under Different Exposure Scenarios To Determine Toxicity Levels</p>

  <p class="footer-copy">Copyrights 2024 | All Rights Reserved</p>
  <p class="footer-page">Page No : 04</p>
</section>

<!-- Slide 05 -->
<section class="slide slide--eps">
  <h1 class="title">EXPANDED POLYSTYRENE DOES NOT<br>POSE A HUMAN HEALTH THREAT</h1>
  <div class="brand"><span class="brand-mark"></span><span class="brand-name">Foam Science<br>Alliance</span></div>
  <p class="sub">EXPANDED POLYSTYRENE FOAM – RESIDUAL STYRENE EMISSIONS</p>

  <div class="emissions">
    <p class="emissions-head emissions-head--scenario">EXPOSURE SCENARIO</p>
    <p class="emissions-head emissions-head--life">CONSUMER STYRENE LIFETIME</p>
    <span class="emissions-split"></span>
    <p class="row-label" style="top:32px">Private Office</p><p class="row-value" style="top:32px">0.05–0.79</p>
    <span class="row-rule" style="top:45px"></span>
    <p class="row-label" style="top:52px">School Classroom</p><p class="row-value" style="top:52px">0.03–0.48</p>
    <span class="row-rule" style="top:65px"></span>
    <p class="row-label" style="top:72px">Home Residence</p><p class="row-value" style="top:72px">0.48–7.33</p>
    <span class="row-rule" style="top:85px"></span>
    <p class="row-label" style="top:92px">State Health Office Safe Harbor<br>Styrene NSRL</p><p class="row-value" style="top:101px">27</p>
  </div>

  <svg class="chart" viewBox="285 80 245 184" role="presentation">
    <rect x="301" y="90" width="211" height="158" fill="#f1f1f1"/>
    <line x1="315" y1="80" x2="315" y2="264" stroke="#d5d5d5" stroke-width=".6"/>
    <line x1="285" y1="233" x2="529" y2="233" stroke="#d5d5d5" stroke-width=".6"/>
    <rect x="317" y="125" width="188" height="108" fill="var(--gold-deep)"/>
    <g stroke="#d9a92a" stroke-width=".4">
      <line x1="317" y1="134" x2="505" y2="134"/><line x1="317" y1="156" x2="505" y2="156"/><line x1="317" y1="177" x2="505" y2="177"/><line x1="317" y1="198" x2="505" y2="198"/><line x1="317" y1="219" x2="505" y2="219"/>
    </g>
    <polygon points="317,228 419,219 430,211 505,211 505,233 317,233" fill="var(--lime)"/>
    <g font-family="Roboto" font-size="5.4" fill="#444" text-anchor="end">
      <text x="311" y="115">30</text><text x="311" y="136">25</text><text x="311" y="158">20</text><text x="311" y="179">15</text><text x="311" y="200">10</text><text x="311" y="221">5</text>
    </g>
    <text x="404" y="158" font-family="Roboto" font-size="8.4" fill="#fff" text-anchor="middle">Styrene NSRL</text>
    <text x="404" y="169" font-family="Roboto" font-size="8.4" fill="#fff" text-anchor="middle">≤27µg/day IS NOT Harmful</text>
    <text x="465" y="227" font-family="Roboto" font-size="8.4" fill="#fff" text-anchor="middle">≤7.3µg/day</text>
    <g font-family="Roboto" font-size="6.8" fill="#333" text-anchor="middle">
      <text x="329" y="243">Office</text><text x="413" y="243">School</text><text x="487" y="244">Residence</text>
    </g>
  </svg>

  <p class="footer-copy">Copyrights 2024 | All Rights Reserved</p>
  <p class="footer-page">Page No : 05</p>
</section>

</body>
</html>
```